Flyer Design Project

Hi There
Im a Photobooth company called Glimmer Kiosk Hire, We rent out PhotoBooth for weddings, Parties and Coperate Functions.
im exbiting at an expo and need some flyers to hand out to our potential customer.
The back of the poster should include our pricing and packages.
We looking for an eye catching fyler, that display all information needed for a potential customer to see what service we offer

It Company

```html
<!DOCTYPE html>
<html lang="en">
<head>
<meta charset="utf-8">
<title>Glimmer Kiosk Hire – Packages &amp; Prices</title>
<link href="https://fonts.googleapis.com/css2?family=Fredoka:wght@600;700&family=Fira+Sans+Condensed:wght@700;800&display=swap" rel="stylesheet">
<style>
  :root {
    --orange: #f6ad1b;
    --orange-deep: #e89a0c;
    --frame: #fddc94;
    --white: #ffffff;
    --backdrop-a: #efe7da;
    --backdrop-b: #d9cfc2;
    --shadow: rgba(60, 40, 10, 0.35);
  }
  * { box-sizing: border-box; margin: 0; padding: 0; }
  html, body { width: 846px; height: 1200px; overflow: hidden; background: var(--frame); }
  .sheet {
    position: relative; width: 846px; height: 1200px;
    background: var(--frame);
    font-family: "Fira Sans Condensed", "Arial Narrow", sans-serif;
  }
  .collage {
    position: absolute; left: 20px; top: 20px; width: 806px; height: 1160px;
    background: linear-gradient(160deg, var(--backdrop-a) 0%, var(--backdrop-b) 45%, var(--backdrop-a) 100%);
    opacity: 0.9;
  }
  .veil { position: absolute; left: 20px; top: 20px; width: 806px; height: 1160px; background: rgba(255,255,255,0.35); }

  .heading {
    position: absolute; font-family: "Fredoka", "Arial Rounded MT Bold", sans-serif; font-weight: 700;
    color: var(--orange); text-align: center;
    -webkit-text-stroke: 1.5px var(--white);
    text-shadow: 2px 3px 3px var(--shadow);
  }
  .heading--main { left: 120px; width: 240px; top: 42px; font-size: 46px; }
  .heading--prices { left: 100px; width: 240px; top: 1098px; font-size: 42px; }
  .tier { top: 58px; width: 120px; font-size: 27px; }
  .price { top: 1108px; width: 120px; font-size: 27px; }
  .col-silver { left: 465px; }
  .col-gold { left: 587px; }
  .col-platinum { left: 706px; }

  .rows { position: absolute; left: 0; top: 118px; width: 846px; }
  .row { position: relative; height: 80.8px; }
  .feature {
    position: absolute; left: 32px; top: 0; width: 406px; height: 62px;
    border-radius: 10px 14px 14px 10px;
    display: flex; flex-direction: column; align-items: center; justify-content: center;
    text-align: center; line-height: 1.02; font-weight: 800; font-size: 21px;
    box-shadow: 2px 4px 5px var(--shadow);
    padding: 0 40px;
  }
  .feature small { font-size: 16px; font-weight: 700; }
  .row--filled .feature { background: var(--orange); color: var(--white); }
  .row--outline .feature { background: var(--white); color: var(--orange); border: 2px solid var(--orange); }

  .box {
    position: absolute; top: -1px; width: 90px; height: 64px; border-radius: 6px;
    box-shadow: 2px 4px 5px var(--shadow);
    display: flex; align-items: center; justify-content: center;
  }
  .box--orange { background: var(--orange); border: 2px solid var(--white); }
  .box--white { background: var(--white); border: 2px solid var(--orange); }
  .box--orange .tick path { stroke: var(--white); }
  .box--white .tick path { stroke: var(--orange); }
  .box.col-silver { left: 480px; transform: rotate(2deg); }
  .box.col-gold { left: 602px; transform: rotate(-3deg); }
  .box.col-platinum { left: 721px; transform: rotate(2.5deg); }
  .tick { width: 46px; height: 40px; }
  .tick path { fill: none; stroke-width: 8; stroke-linecap: round; stroke-linejoin: round; }
</style>
</head>
<body>
<main class="sheet">
  <div class="collage" role="img" aria-label="Collage of photo booth snapshots of smiling guests"></div>
  <div class="veil"></div>

  <h1 class="heading heading--main">Package</h1>
  <div class="heading tier col-silver">Silver</div>
  <div class="heading tier col-gold">Gold</div>
  <div class="heading tier col-platinum">Platinum</div>

  <section class="rows">
    <!-- row 1 -->
    <div class="row row--filled">
      <div class="feature">4 hours of unlimited photos</div>
      <div class="box box--orange col-silver"><svg class="tick" viewBox="0 0 46 40"><path d="M6 21 L18 32 L40 6"/></svg></div>
      <div class="box box--white col-gold"><svg class="tick" viewBox="0 0 46 40"><path d="M6 21 L18 32 L40 6"/></svg></div>
      <div class="box box--orange col-platinum"></div>
    </div>
    <div class="row row--outline">
      <div class="feature">6 hours of unlimited photos</div>
      <div class="box box--white col-silver"></div>
      <div class="box box--orange col-gold"></div>
      <div class="box box--white col-platinum"><svg class="tick" viewBox="0 0 46 40"><path d="M6 21 L18 32 L40 6"/></svg></div>
    </div>
    <div class="row row--filled">
      <div class="feature">Black &amp;White, Color and Sepia photos</div>
      <div class="box box--orange col-silver"><svg class="tick" viewBox="0 0 46 40"><path d="M6 21 L18 32 L40 6"/></svg></div>
      <div class="box box--white col-gold"><svg class="tick" viewBox="0 0 46 40"><path d="M6 21 L18 32 L40 6"/></svg></div>
      <div class="box box--orange col-platinum"><svg class="tick" viewBox="0 0 46 40"><path d="M6 21 L18 32 L40 6"/></svg></div>
    </div>
    <div class="row row--outline">
      <div class="feature">Total customization of strips<small>(names, dates or personalized graphics)</small></div>
      <div class="box box--white col-silver"><svg class="tick" viewBox="0 0 46 40"><path d="M6 21 L18 32 L40 6"/></svg></div>
      <div class="box box--orange col-gold"><svg class="tick" viewBox="0 0 46 40"><path d="M6 21 L18 32 L40 6"/></svg></div>
      <div class="box box--white col-platinum"><svg class="tick" viewBox="0 0 46 40"><path d="M6 21 L18 32 L40 6"/></svg></div>
    </div>
    <div class="row row--filled">
      <div class="feature">Hassel free delivery, setup and removal</div>
      <div class="box box--orange col-silver"><svg class="tick" viewBox="0 0 46 40"><path d="M6 21 L18 32 L40 6"/></svg></div>
      <div class="box box--white col-gold"><svg class="tick" viewBox="0 0 46 40"><path d="M6 21 L18 32 L40 6"/></svg></div>
      <div class="box box--orange col-platinum"><svg class="tick" viewBox="0 0 46 40"><path d="M6 21 L18 32 L40 6"/></svg></div>
    </div>
    <div class="row row--outline">
      <div class="feature">The Prop Box<small>(glasses, wigs, boas, hats, masks, etc)</small></div>
      <div class="box box--white col-silver"><svg class="tick" viewBox="0 0 46 40"><path d="M6 21 L18 32 L40 6"/></svg></div>
      <div class="box box--orange col-gold"><svg class="tick" viewBox="0 0 46 40"><path d="M6 21 L18 32 L40 6"/></svg></div>
      <div class="box box--white col-platinum"><svg class="tick" viewBox="0 0 46 40"><path d="M6 21 L18 32 L40 6"/></svg></div>
    </div>
    <div class="row row--filled">
      <div class="feature">A Guestbook to create a one-of-a-kind masterpiece</div>
      <div class="box box--orange col-silver"></div>
      <div class="box box--white col-gold"><svg class="tick" viewBox="0 0 46 40"><path d="M6 21 L18 32 L40 6"/></svg></div>
      <div class="box box--orange col-platinum"><svg class="tick" viewBox="0 0 46 40"><path d="M6 21 L18 32 L40 6"/></svg></div>
    </div>
    <div class="row row--outline">
      <div class="feature">Copyright-free DVD of ALL Pictures and/or Videos</div>
      <div class="box box--white col-silver"></div>
      <div class="box box--orange col-gold"><svg class="tick" viewBox="0 0 46 40"><path d="M6 21 L18 32 L40 6"/></svg></div>
      <div class="box box--white col-platinum"><svg class="tick" viewBox="0 0 46 40"><path d="M6 21 L18 32 L40 6"/></svg></div>
    </div>
    <div class="row row--filled">
      <div class="feature">Allow guests to email photo’s to themselves</div>
      <div class="box box--orange col-silver"><svg class="tick" viewBox="0 0 46 40"><path d="M6 21 L18 32 L40 6"/></svg></div>
      <div class="box box--white col-gold"><svg class="tick" viewBox="0 0 46 40"><path d="M6 21 L18 32 L40 6"/></svg></div>
      <div class="box box--orange col-platinum"><svg class="tick" viewBox="0 0 46 40"><path d="M6 21 L18 32 L40 6"/></svg></div>
    </div>
    <div class="row row--outline">
      <div class="feature">Guests can instantly upload photos to FRIENDSPACE!!!</div>
      <div class="box box--white col-silver"></div>
      <div class="box box--orange col-gold"></div>
      <div class="box box--white col-platinum"><svg class="tick" viewBox="0 0 46 40"><path d="M6 21 L18 32 L40 6"/></svg></div>
    </div>
    <div class="row row--filled">
      <div class="feature">Unlimited extra copies of strips and 6x4 Prints of guest best shots</div>
      <div class="box box--orange col-silver"></div>
      <div class="box box--white col-gold"></div>
      <div class="box box--orange col-platinum"><svg class="tick" viewBox="0 0 46 40"><path d="M6 21 L18 32 L40 6"/></svg></div>
    </div>
    <div class="row row--outline">
      <div class="feature">Video Messages</div>
      <div class="box box--white col-silver"></div>
      <div class="box box--orange col-gold"></div>
      <div class="box box--white col-platinum"><svg class="tick" viewBox="0 0 46 40"><path d="M6 21 L18 32 L40 6"/></svg></div>
    </div>
  </section>

  <h2 class="heading heading--prices">Prices</h2>
  <div class="heading price col-silver">$1200</div>
  <div class="heading price col-gold">$1400</div>
  <div class="heading price col-platinum">$1700</div>
</main>
</body>
</html>
```